Webdesign for an Health & kirelta studio

We need a new modern and elegant web design for the relaunch of the http://kirelta.at/ website.
The website is for a company which offer all services for a beuty center like epilation, cosmetics and more.
The new website should use big emotional background images and a modern menu.
All in all the website should give a female expression and the design should be clear and not playful.
The existing logo used be used for the new design, the base colours of the existing website could be used optionally.

Industry/Entity Type
It Company
Look and feel
Each slider illustrates characteristics of the customer's brand and the style your logo design should communicate.

```html
<!DOCTYPE html>
<html lang="en">
<head>
<meta charset="utf-8">
<title>Kirelta – Health &amp; Beauty Center</title>
<link href="https://fonts.googleapis.com/css2?family=Open+Sans:wght@300;400;600&family=Pathway+Gothic+One&family=Libre+Baskerville&display=swap" rel="stylesheet">
<style>
:root{
  --nav-bg:#dccab0;
  --nav-text:#4a2f22;
  --accent-red:#c0392b;
  --brown-dark:#3a2420;
  --brown-gallery:#4a3830;
  --brown-footer:#2e2220;
  --cream:#ecdfd0;
  --cream-title:#ecd6b6;
  --muted:#8e5e4a;
  --olive:#8a7340;
  --button:#8a4526;
  --body-text:#4a3a30;
}
*{margin:0;padding:0;box-sizing:border-box}
html,body{width:761px;height:1200px;overflow:hidden;background:#fff}
body{position:relative;font-family:'Open Sans',sans-serif}
.abs{position:absolute}
.nav{left:0;top:0;width:761px;height:37px;background:var(--nav-bg)}
.nav a{position:absolute;top:13px;font-size:9px;font-weight:600;color:var(--nav-text);text-decoration:none;letter-spacing:.3px}
.header{left:0;top:37px;width:761px;height:69px;background:#fff}
.call{left:68px;top:26px;font-size:16px;font-weight:300;color:#444}
.call span{color:var(--accent-red)}
.brand{left:332px;top:14px;display:flex;align-items:center;gap:6px}
.brand i{width:16px;height:16px;border-radius:50%;background:#8a5a44;display:block}
.brand b{font-weight:300;font-size:30px;letter-spacing:3px;color:#6a4a6a}
.social{top:33px;width:15px;height:15px;border-radius:50%;background:var(--accent-red);box-shadow:0 1px 2px rgba(0,0,0,.3)}
.hero{left:0;top:106px;width:761px;height:360px;background:linear-gradient(120deg,#efe7e0 0%,#e6c6ab 35%,#d9a88a 60%,#c9b29c 85%,#a89584 100%)}
.caption{left:63px;top:362px;width:348px;height:84px;background:rgba(245,240,236,.82);text-align:center}
.caption .small{margin-top:9px;font-size:20px;font-weight:400;color:#3a3a3a;letter-spacing:.5px}
.caption .big{margin-top:-4px;font-size:40px;font-weight:400;color:var(--olive);letter-spacing:1px;line-height:44px}
.dot{top:441px;width:8px;height:8px;border-radius:50%;background:#2b2b2b}
.intro{left:0;top:466px;width:761px;height:140px;background:radial-gradient(ellipse at 50% 0%,#4c2e28,var(--brown-dark) 70%);border-top:2px solid #1e1210}
.intro h2{position:absolute;top:23px;width:100%;text-align:center;font-family:'Libre Baskerville',serif;font-weight:400;font-size:16px;color:var(--cream-title)}
.intro p{position:absolute;top:53px;left:120px;width:521px;text-align:center;font-size:8.3px;line-height:14px;color:var(--muted)}
.features{left:0;top:606px;width:761px;height:267px;background:linear-gradient(#f1e8df,var(--cream));border-top:3px solid #fff;border-bottom:3px solid #fff}
.feature{top:565px;width:170px;text-align:center}
.ring{width:134px;height:134px;margin:0 auto;border-radius:50%;background:#fff;padding:8px}
.photo{width:118px;height:118px;border-radius:50%}
.feature h3{margin-top:10px;font-family:'Pathway Gothic One',sans-serif;font-weight:400;font-size:24px;color:#5a3a2a;letter-spacing:-.5px}
.feature p{margin-top:8px;font-size:7.7px;line-height:12.7px;color:var(--body-text)}
.more{display:block;width:37px;height:37px;margin:16px auto 0;border-radius:50%;background:var(--button);border:2px solid #c8906a;font-family:'Pathway Gothic One',sans-serif;font-size:14px;line-height:33px;color:#f4e2cf;text-decoration:none}
.gallery{left:0;top:876px;width:761px;height:256px;background:var(--brown-gallery)}
.gallery h2{position:absolute;left:84px;top:34px;font-family:'Libre Baskerville',serif;font-weight:400;font-size:20px;color:var(--cream-title)}
.thumb{top:83px;width:89px;height:89px;border:3px solid #fff}
.arrow{top:193px;width:23px;height:22px;display:flex;align-items:center;justify-content:center}
.footer{left:0;top:1132px;width:761px;height:68px;background:var(--brown-footer);color:#fff;font-size:7.6px;line-height:13px}
.footer .left{position:absolute;left:63px;top:18px}
.footer .right{position:absolute;right:98px;top:10px;text-align:right}
</style>
</head>
<body>
<nav class="abs nav">
  <a style="left:64px" href="#">HOME</a>
  <a style="left:116px" href="#">CATEGORIES</a>
  <a style="left:203px" href="#">FAQ'S</a>
  <a style="left:259px" href="#">GALLERY</a>
  <a style="left:326px" href="#">SHOPPING CART</a>
  <a style="left:424px" href="#">OUR PARTNERS</a>
  <a style="left:519px" href="#">CONTACT US</a>
  <a style="left:602px" href="#">SITEMAP</a>
</nav>

<header class="abs header">
  <div class="abs call"><span>Call Us :</span> +123 555 0148</div>
  <div class="abs brand"><i></i><b>kirelta</b></div>
  <span class="abs social" style="left:633px"></span>
  <span class="abs social" style="left:656px"></span>
  <span class="abs social" style="left:679px"></span>
</header>

<section class="abs hero" role="img" aria-label="Woman relaxing during a facial massage, hands cradling her face"></section>
<div class="abs caption">
  <div class="small">SPECIAL CARE</div>
  <div class="big">SOLUTIONS</div>
</div>
<span class="abs dot" style="left:663px"></span>
<span class="abs dot" style="left:675px"></span>
<span class="abs dot" style="left:687px;background:#7a8a4a"></span>

<section class="abs intro">
  <h2>LET US TAKE YOU TO THE PARADISE!</h2>
  <p>Casrolem atur aut oditaut. onsequuntur magni dolores eo qui ratione voluptatemsequi nesciunt, neqporro quisquam estquis dolorem ipsumuia dolonsectetur, adipisci velited quia non numquam eius modi tempora.</p>
</section>

<section class="abs features"></section>
<div class="abs feature" style="left:100px">
  <div class="ring"><div class="photo" role="img" aria-label="Woman relaxing beside candles and stones" style="background:linear-gradient(135deg,#f0e4dc,#d98a5a 60%,#8a5a44)"></div></div>
  <h3>SKIN CARE</h3>
  <p>Lorem ipsum dolor sit amet, consectetur adipiscing elit. Sed luctus, felis et vulpu-tate pulvinar, sapien risus ornare lorem, quis pharetra tellus mauris non augue.</p>
  <a class="more" href="#">MORE</a>
</div>
<div class="abs feature" style="left:290px">
  <div class="ring"><div class="photo" role="img" aria-label="Feet among rose petals" style="background:linear-gradient(135deg,#f4ece8,#e8b6a8 55%,#d07080)"></div></div>
  <h3>OUR SERVICES</h3>
  <p>Lorem ipsum dolor sit amet, consectetur adipiscing elit. Sed luctus, felis et vulpu-tate pulvinar, sapien risus ornare lorem, quis pharetra tellus mauris non augue.</p>
  <a class="more" href="#">MORE</a>
</div>
<div class="abs feature" style="left:480px">
  <div class="ring"><div class="photo" role="img" aria-label="Aromatherapy candles and leaves" style="background:linear-gradient(135deg,#4a2a20,#8a6a4a 55%,#c8c098)"></div></div>
  <h3>AROMATHERAPY</h3>
  <p>Lorem ipsum dolor sit amet, consectetur adipiscing elit. Sed luctus, felis et vulpu-tate pulvinar, sapien risus ornare lorem, quis pharetra tellus mauris non augue.</p>
  <a class="more" href="#">MORE</a>
</div>
<svg class="abs" style="left:692px;top:849px" width="10" height="12" viewBox="0 0 10 12"><path d="M5 11V1M1 5l4-4 4 4" fill="none" stroke="#d8c0a8" stroke-width="1.2"/></svg>

<section class="abs gallery">
  <h2>PHOTO GALLERY</h2>
  <div class="abs thumb" style="left:84px;background:linear-gradient(135deg,#6a4a4a,#b08a8a)" role="img" aria-label="Portrait of a woman with curly hair"></div>
  <div class="abs thumb" style="left:204px;background:linear-gradient(135deg,#3a6a3a,#d8a888)" role="img" aria-label="Woman with a flower relaxing at a spa"></div>
  <div class="abs thumb" style="left:322px;background:linear-gradient(135deg,#e8e8e0,#d8b8a0)" role="img" aria-label="Woman in a towel resting"></div>
  <div class="abs thumb" style="left:449px;background:linear-gradient(135deg,#2a2a2a,#b08060 60%,#eeeeee)" role="img" aria-label="Woman applying face cream"></div>
  <div class="abs thumb" style="left:571px;background:linear-gradient(135deg,#6a4a3a,#c8a070)" role="img" aria-label="Hot stone massage"></div>
  <div class="abs arrow" style="left:87px;background:#1e1612"><svg width="6" height="8" viewBox="0 0 6 8"><path d="M4.5 1L1.5 4l3 3" fill="none" stroke="#fff" stroke-width="1.4"/></svg></div>
  <div class="abs arrow" style="left:110px;background:#c8b8a0"><svg width="6" height="8" viewBox="0 0 6 8"><path d="M1.5 1l3 3-3 3" fill="none" stroke="#fff" stroke-width="1.4"/></svg></div>
</section>

<footer class="abs footer">
  <div class="left">Copyright © 2014 - Kirelta. - All Rights Reserved<br>Powered by: kirelta studio.</div>
  <div class="right">Toll-Free: (800) 555-0193<br>Email: hello@kirelta-mail.com<br>48 Linden Row• Maple Grove, OK 70000</div>
</footer>
</body>
</html>
```